Carte d'affaire bilingue

Nous avons besoin d'une carte d'affaire pour notre entreprise spécialisée en vente et achat de terrain. Nous sommes une agence immobilière et nous voulons une carte avec le recto en Français et le verso en anglais. Nous voulons une image sobre et épurée. Nous avons de la clientèle internationale et nous voulons une carte très professionnelle mais qui se démarque. Nous voulons cibler une clientèle commerciale, industrielle, contracteurs et promoteurs immobiliers.

Hi everybody, we saw all your conception and we are approching of what we like but the "WOW" is missing.

We love the little sign to specify (phone or email) but we can put them in a square to make like our logo, we love also dark gray not lite gray, we also love the stainless lines. In our logo you can see a little sign +. For us is signyfy " Always further" so if you can put many little +++++ in the conception somewhere very discret it will be appreciate. We also like a kind of round that make a magnyfying glass, because we search land we found opportunity.

Thank you

Reason: I ask different things in the last day but no one do what i am asking for. For the conception # 3016702 that we love we ask changes.

We like simplicity, urban design, corporate, international. The card must have one side in french and the other side in english. We like dark gray,silver, and a little bit of green.

Target Market(s)

Investors, developers, construction builders, etc...

Font styles to use
Serif
Sans Serif

Requirements
Must have
• logo
La mention: Agence immobilière (Francais) / Real Estate Agency (anglais)
Sous le nom: Courtier immobilier agréé (Français) / Real Estate Broker

```html
<!DOCTYPE html>
<html lang="en">
<head>
<meta charset="utf-8">
<title>Terra Field – Business Cards</title>
<link rel="stylesheet" href="https://fonts.googleapis.com/css2?family=Crimson+Text:wght@400;600;700&display=swap">
<style>
  :root {
    --bg: #e4e5e4;
    --card: #ffffff;
    --green: #0b6b3a;
    --ink: #2b2b2b;
    --gray: #6d6f71;
    --shadow: rgba(0,0,0,0.18);
  }
  * { margin: 0; padding: 0; box-sizing: border-box; }
  html, body { width: 1200px; height: 926px; overflow: hidden; }
  body {
    background: var(--bg);
    font-family: "Crimson Text", Georgia, serif;
    color: var(--ink);
    position: relative;
  }
  .card {
    position: absolute;
    width: 570px;
    height: 326px;
    background: var(--card);
    box-shadow: 0 6px 18px var(--shadow);
    overflow: hidden;
  }
  .card--brand { left: 315px; top: 112px; }
  .card--en { left: 20px; top: 488px; }
  .card--fr { left: 610px; top: 488px; }

  .brand {
    display: flex;
    align-items: center;
    gap: 10px;
    color: var(--gray);
    font-weight: 600;
    text-transform: uppercase;
    letter-spacing: 2px;
    white-space: nowrap;
  }
  .brand__square { background: var(--green); flex: none; }
  .card--brand .brand {
    position: absolute;
    left: 50%; top: 50%;
    transform: translate(-50%, -50%);
    font-size: 46px;
    gap: 14px;
  }
  .card--brand .brand__square { width: 50px; height: 50px; }

  .card--contact .brand {
    position: absolute;
    left: 32px; top: 28px;
    font-size: 25px;
  }
  .card--contact .brand__square { width: 28px; height: 28px; }

  .contact-list {
    position: absolute;
    left: 32px; top: 98px;
    list-style: none;
    font-size: 14px;
    line-height: 17px;
    white-space: nowrap;
  }
  .contact-list__label { color: var(--green); font-weight: 700; }

  .person {
    position: absolute;
    right: 32px; top: 76px;
    text-align: right;
    white-space: nowrap;
  }
  .person__name {
    color: var(--green);
    font-size: 18px;
    font-weight: 600;
    letter-spacing: 1px;
    text-transform: uppercase;
    line-height: 22px;
  }
  .person__title { font-size: 13px; color: var(--gray); line-height: 15px; }
  .person__role { font-size: 11.5px; font-weight: 700; text-transform: uppercase; line-height: 15px; }

  .address {
    position: absolute;
    left: 312px; top: 145px;
    display: flex;
    gap: 7px;
  }
  .address__icon { width: 16px; height: 15px; flex: none; }
  .address__lines {
    border-left: 1.5px solid var(--green);
    padding-left: 8px;
    font-size: 14px;
    font-weight: 600;
    line-height: 19px;
    letter-spacing: 0.5px;
    text-transform: uppercase;
    white-space: nowrap;
  }

  .wave { position: absolute; left: 0; top: 0; width: 570px; height: 326px; }
  .agency {
    position: absolute;
    right: 32px; bottom: 30px;
    color: #fff;
    font-size: 21px;
    letter-spacing: 1.2px;
    text-transform: uppercase;
    white-space: nowrap;
  }
</style>
</head>
<body>

<section class="card card--brand">
  <div class="brand"><span class="brand__square"></span>Terra Field</div>
</section>

<section class="card card--contact card--en" lang="en">
  <svg class="wave" viewBox="0 0 700 400" preserveAspectRatio="none" aria-hidden="true">
    <path d="M0,225 C110,265 240,300 420,292 C560,286 640,262 700,240 L700,400 L0,400 Z" fill="var(--green)"/>
    <path d="M30,262 C160,310 330,318 470,300 C580,287 650,266 700,250 L700,262 C640,280 570,300 470,311 C320,328 150,318 30,262 Z" fill="#ffffff"/>
  </svg>
  <div class="brand"><span class="brand__square"></span>Terra Field</div>
  <ul class="contact-list">
    <li><span class="contact-list__label">phone:</span> 514-555-0142</li>
    <li><span class="contact-list__label">fax:</span> 450-555-0187</li>
    <li><span class="contact-list__label">toll free:</span> 1-866-555-0199</li>
    <li><span class="contact-list__label">email:</span> m.ouellet@terrafield.com</li>
    <li><span class="contact-list__label">web:</span> www.terrafield.com</li>
  </ul>
  <div class="person">
    <div class="person__name">Mireille Ouellet</div>
    <div class="person__title">Real estate broker, D.A.</div>
    <div class="person__role">Vice President</div>
  </div>
  <div class="address">
    <svg class="address__icon" viewBox="0 0 20 18" aria-hidden="true">
      <path d="M10,1 L19,9 L16.5,9 L16.5,17 L12,17 L12,12 L8,12 L8,17 L3.5,17 L3.5,9 L1,9 Z" fill="var(--green)"/>
    </svg>
    <div class="address__lines">210 Rue des Érables,<br>3E, Laval, QC,<br>H7X 1B4</div>
  </div>
  <div class="agency">Real Estate Agency</div>
</section>

<section class="card card--contact card--fr" lang="fr">
  <svg class="wave" viewBox="0 0 700 400" preserveAspectRatio="none" aria-hidden="true">
    <path d="M0,225 C110,265 240,300 420,292 C560,286 640,262 700,240 L700,400 L0,400 Z" fill="var(--green)"/>
    <path d="M30,262 C160,310 330,318 470,300 C580,287 650,266 700,250 L700,262 C640,280 570,300 470,311 C320,328 150,318 30,262 Z" fill="#ffffff"/>
  </svg>
  <div class="brand"><span class="brand__square"></span>Terra Field</div>
  <ul class="contact-list">
    <li><span class="contact-list__label">tél. :</span> 514-555-0142</li>
    <li><span class="contact-list__label">téléc. :</span> 450-555-0187</li>
    <li><span class="contact-list__label">sans frais :</span> 1-866-555-0199</li>
    <li><span class="contact-list__label">courriel :</span> m.ouellet@terrafield.com</li>
    <li><span class="contact-list__label">web :</span> www.terrafield.com</li>
  </ul>
  <div class="person">
    <div class="person__name">Mireille Ouellet</div>
    <div class="person__title">Courtier immobilier agréé, D.A.</div>
    <div class="person__role">Vice-présidente</div>
  </div>
  <div class="address">
    <svg class="address__icon" viewBox="0 0 20 18" aria-hidden="true">
      <path d="M10,1 L19,9 L16.5,9 L16.5,17 L12,17 L12,12 L8,12 L8,17 L3.5,17 L3.5,9 L1,9 Z" fill="var(--green)"/>
    </svg>
    <div class="address__lines">210 Rue des Érables,<br>3E, Laval, QC,<br>H7X 1B4</div>
  </div>
  <div class="agency">Agence immobilière</div>
</section>

</body>
</html>
```